Law Firm Stationery Design - Traditional Meets Intuitive

Looking for a modern, yet classic, law firm stationery design. Simplicity is desired, but great ideas are encouraged. See attachment for company information. We utilize a variety of non-traditional legal tools to bring a different perspective to each of our client's particular situation. Final design should communicate classic values with intuitive, unique solutions.

Industry/Entity Type

Law Firm

Requirements
Should not have
• - No typical legal icons
• - No Tag Line!
• - DO NOT WANT WHAT WE ALREADY HAVE

```html
<!DOCTYPE html>
<html lang="en">
<head>
<meta charset="utf-8">
<title>Veritane Law LLC — Stationery</title>
<link href="https://fonts.googleapis.com/css2?family=Tinos:wght@400;700&family=Open+Sans:wght@400;600&display=swap" rel="stylesheet">
<style>
  :root {
    --brand-blue: #1c5486;
    --ink: #1a1a1a;
    --paper: #ffffff;
    --backdrop: #8c8c8c;
    --muted: #333333;
  }
  * { margin: 0; padding: 0; box-sizing: border-box; }
  html, body { width: 1200px; height: 876px; overflow: hidden; }
  body { background: var(--backdrop); position: relative; font-family: "Open Sans", Arial, sans-serif; }

  .sheet { position: absolute; background: var(--paper); overflow: hidden; }
  .wordmark {
    font-family: "Tinos", "Times New Roman", serif;
    font-weight: 700;
    color: var(--brand-blue);
    letter-spacing: 0.04em;
    white-space: nowrap;
  }
  .top-rule { position: absolute; left: 0; top: 0; width: 100%; background: var(--brand-blue); }

  /* Letterhead */
  .letterhead { left: 67px; top: 94px; width: 498px; height: 704px; }
  .letterhead .top-rule { height: 6px; }
  .letterhead .wordmark { position: absolute; top: 36px; left: 0; width: 100%; text-align: center; font-size: 23px; }
  .letter-body {
    position: absolute; left: 51px; top: 180px; width: 406px;
    font-family: "Tinos", "Times New Roman", serif; font-size: 11.2px; line-height: 12.8px; color: var(--ink);
  }
  .letter-body p { margin-bottom: 12.8px; }
  .letter-body .signoff { margin-top: 25px; margin-bottom: 25px; }
  .letter-footer {
    position: absolute; left: 0; bottom: 0; width: 100%; height: 26px; background: var(--brand-blue);
    color: #fff; font-size: 9.2px; line-height: 26px; text-align: center; letter-spacing: 0.01em;
  }

  /* Business cards */
  .card-front { left: 623px; top: 127px; width: 215px; height: 121px; }
  .card-front .wordmark { position: absolute; left: 0; width: 100%; top: 50px; text-align: center; font-size: 11.5px; }
  .card-back { left: 872px; top: 130px; width: 216px; height: 120px; }
  .card-back .top-rule { height: 3px; }
  .card-back .wordmark { position: absolute; right: 12px; top: 11px; font-size: 8px; }
  .card-name { position: absolute; left: 0; width: 100%; top: 45px; text-align: center; color: var(--brand-blue); font-weight: 600; font-size: 10.5px; line-height: 1.1; }
  .card-title { position: absolute; left: 0; width: 100%; top: 57px; text-align: center; color: var(--muted); font-size: 6.4px; }
  .card-address { position: absolute; left: 15px; top: 88px; font-size: 5.2px; line-height: 6.4px; color: var(--muted); }
  .card-phone { position: absolute; right: 12px; top: 98px; font-size: 5.2px; color: var(--muted); }
  .label { color: var(--brand-blue); }
  .card-back .bottom-band { position: absolute; left: 0; bottom: 0; width: 100%; height: 9px; background: var(--brand-blue); }

  /* Envelope back */
  .envelope-back { left: 623px; top: 282px; width: 507px; height: 244px; }
  .envelope-back .top-rule { height: 4px; }
  .envelope-flap { position: absolute; left: 0; top: 0; }
  .envelope-back .wordmark { position: absolute; left: 0; width: 100%; top: 24px; text-align: center; font-size: 22px; }
  .envelope-url { position: absolute; left: 0; width: 100%; top: 216px; text-align: center; font-size: 12px; color: var(--ink); }

  /* Envelope front */
  .envelope-front { left: 623px; top: 551px; width: 507px; height: 245px; }
  .envelope-front .top-rule { height: 6px; }
  .envelope-front .wordmark { position: absolute; left: 27px; top: 27px; font-size: 21px; }
  .return-note { position: absolute; left: 27px; top: 218px; font-size: 7.8px; color: var(--ink); }
  .return-band { position: absolute; left: 0; bottom: 0; width: 100%; height: 13px; background: var(--brand-blue); color: #fff; font-size: 7.6px; line-height: 13px; padding-left: 27px; }
</style>
</head>
<body>

<section class="sheet letterhead">
  <div class="top-rule"></div>
  <div class="wordmark">VERITANE LAW LLC</div>
  <div class="letter-body">
    <p>Dear Ms. Harlow:</p>
    <p>Nothing is as exciting as getting ready for game day.</p>
    <p>The players warming up, the buzz of the crowd as they enter the park, even the smell of the stadium, all make for an electrically charged atmosphere. I’ve seen if first hand, and I love it.</p>
    <p>I’ve been around professional sports since I was a child. My father worked as a National Baseball League scout for more than 35 years. Even more importantly, I had the pleasure of spending this past summer as an intern for the Riverton Ironclads minor league baseball team.</p>
    <p>It was an amazing experience. I interned in the Public/Media Relations department and had a chance to try my hand at an incredible variety of projects. I worked with Quillfield Broadcast Group as they covered the play of Dale Ruston Jr. and a Hawks/Comets Legends game. I handled all our player appearances. I even set up and ran our first baseball camp. I usually put in 80 hours a week and couldn’t get enough!</p>
    <p>The Ironclads experience, in addition to work for the Lakeshore Wolves and my Sports Management major, all have me extremely interested in pursing a career as an Sports Marketing upon graduation.</p>
    <p>I would love to talk with you more about my passion, my background, and your organization. I look forward to touching base with you soon.</p>
    <p class="signoff">Regards,</p>
    <p>Maren Cole</p>
  </div>
  <footer class="letter-footer">18 Foundry Lane, Suite 300 Halton, MA 02190 &nbsp;|&nbsp; Phone: &nbsp;555-014-2200 &nbsp;|&nbsp; www.veritanelaw.com</footer>
</section>

<section class="sheet card-front">
  <div class="wordmark">VERITANE LAW LLC</div>
</section>

<section class="sheet card-back">
  <div class="top-rule"></div>
  <div class="wordmark">VERITANE LAW LLC</div>
  <div class="card-name">Daniel Hart</div>
  <div class="card-title">President</div>
  <div class="card-address"><span class="label">Address</span><br>18 Foundry Lane, Suite 300<br>Halton, MA 02190</div>
  <div class="card-phone"><span class="label">Phone</span>&nbsp; 555-014-2200</div>
  <div class="bottom-band"></div>
</section>

<section class="sheet envelope-back">
  <svg class="envelope-flap" width="507" height="75" viewBox="0 0 507 75" aria-hidden="true">
    <path d="M2 4 Q10 50 30 62 Q40 70 70 70 L437 70 Q467 70 477 62 Q497 50 505 4" fill="none" stroke="#d9d9d9" stroke-width="1.5"/>
  </svg>
  <div class="top-rule"></div>
  <div class="wordmark">VERITANE LAW LLC</div>
  <div class="envelope-url">www.veritanelaw.com</div>
</section>

<section class="sheet envelope-front">
  <div class="top-rule"></div>
  <div class="wordmark">VERITANE LAW LLC</div>
  <div class="return-note">If undelivered, please return to:</div>
  <div class="return-band">18 Foundry Lane, Suite 300 Halton, MA 02190</div>
</section>

</body>
</html>
```